School Signage

I am wanting designs for signs completed that prompt students of the school requirements for hats, preparation and play.

I've uploaded rough examples of what we're after, but we would like them stylised and better than the example, including:
- A stylised logo/graphic for the 'Wallumba 1, 2, 3'
- Clear, crisp signage for the words.
- Graphics that reinforce the message of the sign.

We're after three signs:
- One that will be located on the oval to prompt hat use.
- One that will be near the entry prompting the morning routine (please make this one landscape with instructions for 'on time' on one side, and 'late' on the other).
- One that will be located within the school prompting readiness for class.

```html
<!DOCTYPE html>
<html lang="en">
<head>
<meta charset="utf-8">
<title>Are you ready for Class? – Wallumba 1, 2, 3</title>
<link href="https://fonts.googleapis.com/css2?family=Roboto:wght@500;700;900&display=swap" rel="stylesheet">
<style>
  :root {
    --green: #1c4a1e;
    --green-soft: #2a5c2c;
    --yellow: #f6e81b;
    --white: #ffffff;
    --stage: #ededed;
    --motif: #efe9d6;
  }
  * { box-sizing: border-box; margin: 0; padding: 0; }
  html, body { width: 1200px; height: 567px; overflow: hidden; }
  body {
    background: var(--stage);
    font-family: 'Roboto', Arial, sans-serif;
    color: var(--green);
    position: relative;
  }
  .poster {
    position: absolute;
    left: 413px; top: 19px;
    width: 374px; height: 528px;
    background: var(--white);
    overflow: hidden;
    box-shadow: 0 4px 14px rgba(0,0,0,0.18);
  }
  .header {
    position: absolute; left: 0; top: 0;
    width: 100%; height: 116px;
    background: var(--green);
    text-align: center;
  }
  .header-art {
    position: absolute; top: 0; height: 56px; width: 90px;
    background: linear-gradient(160deg, var(--green-soft), var(--green));
  }
  .header-art.left { left: 0; border-bottom-right-radius: 60px; }
  .header-art.right { right: 0; border-bottom-left-radius: 60px; }
  .kicker {
    position: absolute; left: 0; right: 0; top: 16px;
    font-size: 25px; font-weight: 700; color: var(--white);
    letter-spacing: 0.1px;
  }
  .title {
    position: absolute; left: 0; right: 0; top: 38px;
    font-size: 40px; font-weight: 900; color: var(--yellow);
    line-height: 1;
  }
  .routine-badge {
    position: absolute; left: 60px; top: 94px;
    width: 253px; height: 46px;
    background: var(--yellow);
    border-radius: 6px;
    box-shadow: -3px 3px 0 var(--green);
    display: flex; align-items: center; justify-content: center; gap: 6px;
    font-weight: 700;
  }
  .routine-badge .name { font-size: 21px; }
  .routine-badge .steps { font-size: 31px; }
  .motif {
    position: absolute; left: 0; top: 215px;
    width: 374px; height: 190px;
    background: radial-gradient(ellipse at 70% 45%, var(--motif), rgba(239,233,214,0) 70%);
    opacity: 0.8;
  }
  .steps-list { list-style: none; }
  .step {
    position: absolute; left: 33px;
    height: 56px; width: 330px;
  }
  .step-num {
    position: absolute; left: 0; top: 14px;
    width: 48px; height: 30px;
    background: var(--yellow);
    border-radius: 3px;
    font-size: 24px; font-weight: 900;
    padding-left: 8px; line-height: 30px;
  }
  .step-icon {
    position: absolute; left: 43px; top: 0;
    width: 56px; height: 56px;
  }
  .step-label {
    position: absolute; left: 108px; top: 11px;
    font-size: 27px; font-weight: 700; white-space: nowrap;
  }
  .step-note {
    position: absolute; left: 0; top: 50px; width: 100%;
    padding-left: 140px;
    font-size: 14px; font-weight: 500; white-space: nowrap;
  }
  .footer {
    position: absolute; left: 0; top: 424px;
    width: 100%; height: 68px;
    background: var(--green);
  }
  .footer-art {
    position: absolute; left: 0; top: 18px; width: 105px; height: 40px;
    background: linear-gradient(90deg, var(--green-soft), var(--green));
    border-top-right-radius: 40px;
  }
  .values {
    position: absolute; left: 105px; top: 10px;
    width: 176px; height: 49px;
    background: var(--yellow);
    border-radius: 4px;
    padding: 10px 0 0 10px;
  }
  .values-title { font-size: 17px; font-weight: 700; line-height: 1; }
  .values-sub { font-size: 8.5px; font-weight: 700; margin-top: 3px; }
  .stripe-yellow {
    position: absolute; left: 0; top: 499px;
    width: 100%; height: 8px; background: var(--yellow);
  }
  .school-mark {
    position: absolute; left: 262px; top: 408px;
    width: 90px; height: 84px;
    text-align: center;
  }
  .school-mark .dot {
    width: 44px; height: 44px; border-radius: 50%;
    background: var(--yellow);
    margin: 0 auto;
  }
  .school-mark .school-name {
    margin-top: 4px;
    font-size: 10px; font-weight: 700; line-height: 1.15;
    color: var(--white); text-transform: uppercase;
  }
</style>
</head>
<body>
  <main class="poster">
    <header class="header">
      <div class="header-art left" role="img" aria-label="Dot-art pattern"></div>
      <div class="header-art right" role="img" aria-label="Dot-art pattern"></div>
      <p class="kicker">Are you ready for</p>
      <h1 class="title">Class?</h1>
    </header>
    <div class="routine-badge"><span class="name">The Wallumba</span><span class="steps">1, 2, 3</span></div>

    <div class="motif" role="img" aria-label="Faint native flora artwork"></div>

    <ol class="steps-list">
      <li class="step" style="top:184px">
        <span class="step-num">1.</span>
        <svg class="step-icon" viewBox="0 0 56 56" aria-hidden="true">
          <circle cx="28" cy="28" r="26" fill="#fff" stroke="var(--green)" stroke-width="3"/>
          <rect x="17" y="17" width="22" height="15" rx="1.5" fill="none" stroke="var(--green)" stroke-width="3"/>
          <path d="M13 35 H43 L40 40 H16 Z" fill="var(--green)"/>
        </svg>
        <span class="step-label">Latop/workbook</span>
      </li>
      <li class="step" style="top:251px">
        <span class="step-num">2.</span>
        <svg class="step-icon" viewBox="0 0 56 56" aria-hidden="true">
          <circle cx="28" cy="28" r="26" fill="#fff" stroke="var(--green)" stroke-width="3"/>
          <rect x="27" y="12" width="14" height="24" rx="3" fill="var(--green)" transform="rotate(15 34 24)"/>
          <circle cx="34" cy="19" r="2.5" fill="#fff"/>
          <ellipse cx="24" cy="37" rx="12" ry="5" fill="var(--green)"/>
          <rect x="12" y="37" width="24" height="6" fill="var(--green)"/>
          <ellipse cx="24" cy="43" rx="12" ry="4" fill="var(--green)"/>
        </svg>
        <span class="step-label">Phone in Pouchlok</span>
      </li>
      <li class="step" style="top:321px">
        <span class="step-num">3.</span>
        <svg class="step-icon" viewBox="0 0 56 56" aria-hidden="true">
          <circle cx="28" cy="28" r="26" fill="#fff" stroke="var(--green)" stroke-width="3"/>
          <path d="M16 34 C16 22 21 15 28 15 C35 15 40 22 40 34 Z" fill="var(--green)"/>
          <path d="M28 15 V34" stroke="#fff" stroke-width="1.5"/>
          <path d="M12 35 H44 V39 H12 Z" fill="var(--green)"/>
        </svg>
        <span class="step-label">Correct uniform</span>
        <span class="step-note">(including hat)</span>
      </li>
    </ol>

    <footer class="footer">
      <div class="footer-art" role="img" aria-label="Dot-art wave pattern"></div>
      <div class="values">
        <p class="values-title">Curiosity and Drive</p>
        <p class="values-sub">Wallumba Learner Values</p>
      </div>
    </footer>
    <div class="stripe-yellow"></div>
    <div class="school-mark">
      <div class="dot"></div>
      <p class="school-name">Wallumba<br>State High</p>
    </div>
  </main>
</body>
</html>
```